Web Design Project - veltrimo

I'm building an agency for marketing solutions but also medical education and patients education for pharmaceutical companies, medical societies and patient advocacy groups. We want to be perceived as the most innovative in the market. We work through design thinking solutions for campaigns and services.
I love some websites based on Swiss style design like www.plorvex.net
We are a small group of designers, physicians and creatives working together to deliver the best experiences in our market.
We decided to also use design crowd expecting that we maybe found a great idea we didn't thought about yet.
Updates

I'm extending it for more 2 weeks

Reason: I need the best design you can. Only PSD. No code needed. Love Swiss style, like qualdor 5 and plorvex.net I'm extending the deadline until get something great. Willing to extend as much as needed.

Target Market(s)

Pharmaceutical companies, physicians, medical societies, patients advocacy groups

Industry/Entity Type

Pharmaceutical

Font styles to use
Other font styles liked:
• Helvetia family

Colors

Designer to choose colors to be used in the design.

Requirements
Must have
• Must be innovative like www.plorvex.net
Nice to have
• Cool menus
Should not have
• Not to appear too much Comercial. We like to be a boutique in this market. Craftsmen working with less clients at time but delivering precious stones.

```html
<!DOCTYPE html>
<html lang="en">
<head>
<meta charset="utf-8">
<title>veltrimo</title>
<link rel="stylesheet" href="https://fonts.googleapis.com/css2?family=Open+Sans:wght@300;400;600&family=Saira+Condensed:wght@700&display=swap">
<style>
:root{
  --teal:#17a398;
  --page:#252525;
  --tile:#3b3b3b;
  --tile-text:#a9a9a9;
  --heading:#e6e6e6;
  --white:#ffffff;
  --muted:#9a9a9a;
  --rule:#3a3a3a;
}
*{margin:0;padding:0;box-sizing:border-box}
html,body{width:1200px;height:2250px;overflow:hidden}
body{background:var(--page);font-family:"Open Sans",Arial,sans-serif;color:var(--tile-text);position:relative}
.site-header{position:absolute;left:0;top:0;width:1200px;height:80px;background:var(--teal)}
.brand{position:absolute;left:100px;top:12px;font-family:"Saira Condensed",Arial,sans-serif;font-weight:700;font-size:50px;line-height:56px;color:var(--white);letter-spacing:1px}
.main-nav{position:absolute;top:22px;left:900px;display:flex;gap:22px}
.main-nav svg{width:34px;height:34px;fill:var(--white)}
.tile,.media{position:absolute}
.tile{background:var(--tile);padding:30px 27px}
.tile h2{font-weight:300;font-size:36px;line-height:40px;color:var(--heading);margin-bottom:18px}
.tile p{font-size:14.5px;line-height:27px}
.media{}
.welcome h1{font-weight:300;font-size:52px;line-height:60px;color:var(--heading);margin:0 0 14px}
.arrow{position:absolute;width:0;height:0;border:16px solid transparent}
.arrow.down{border-top-color:var(--tile);bottom:-32px;left:192px}
.arrow.left{border-right-color:var(--tile);left:-32px}
.arrow.right{border-left-color:var(--tile);right:-32px}
.contacts{position:absolute;top:1946px;left:0;width:1200px;height:63px}
.contact-icon{position:absolute;top:16px;width:32px;height:32px;fill:#8a8a8a}
.contact-box{position:absolute;top:0;height:63px;background:var(--tile);font-size:13.5px;line-height:20px;color:#c8c8c8;padding:0 12px;display:flex;align-items:center}
.divider{position:absolute;left:99px;top:2051px;width:1002px;height:1px;background:var(--rule)}
.footer-nav{position:absolute;top:2085px;width:1200px;text-align:center;font-size:13.5px;color:#c8c8c8}
.footer-nav span{margin:0 9px;color:#777}
.copyright{position:absolute;top:2118px;width:1200px;text-align:center;font-size:13.5px;color:#b0b0b0}
.social{position:absolute;top:2172px;width:33px;height:33px;background:#e9e9e9;border-radius:3px}
</style>
</head>
<body>
<header class="site-header">
  <div class="brand">VELTRIMO</div>
  <nav class="main-nav">
    <svg viewBox="0 0 24 24"><path d="M12 3 2 12h3v9h5v-6h4v6h5v-9h3z"/></svg>
    <svg viewBox="0 0 24 24"><circle cx="12" cy="7" r="5"/><path d="M2 22c0-6 4-9 10-9s10 3 10 9z"/></svg>
    <svg viewBox="0 0 24 24"><path d="M12 8a4 4 0 1 0 0 8 4 4 0 0 0 0-8zm9 5.5v-3l-2.6-.5-.7-1.7 1.5-2.2-2.1-2.1-2.2 1.5-1.7-.7L13.5 2h-3l-.5 2.6-1.7.7L6.1 3.8 4 5.9l1.5 2.2-.7 1.7L2 10.5v3l2.6.5.7 1.7-1.5 2.2L5.9 20l2.2-1.5 1.7.7.7 2.8h3l.5-2.6 1.7-.7 2.2 1.5 2.1-2.1-1.5-2.2.7-1.7z"/></svg>
    <svg viewBox="0 0 24 24"><path d="M3 3h5l2 5-3 2c1.5 3 4 5.5 7 7l2-3 5 2v5c-10 0-18-8-18-18z"/></svg>
  </nav>
</header>

<section class="tile welcome" style="left:99px;top:153px;width:303px;height:437px">
  <h1>Welcome</h1>
  <p>Integer eu lorem commodo, semper lectus nec, venenatis arcu. Aenean turpis orci, laoreet a bibendum in, tempus id odio. Aliquam efficitur, ante quis varius gravida, diam velit suscipit diam, tincidunt elementum velit nibh id nunc. Maecenas laoreet tempus semper. Aliquam a sodales magna. Donec nec velit a turpis molestie molestie quis sit amet neque.</p>
</section>
<div class="media" role="img" aria-label="Team working around a wooden desk with computers and papers" style="left:412px;top:153px;width:689px;height:437px;background:linear-gradient(135deg,#9a6a3e,#b98553 45%,#7d5431)"></div>

<section class="tile" style="left:99px;top:602px;width:417px;height:186px">
  <h2>Marketing Solution</h2>
  <p>Aliquam efficitur, ante quis varius gravida, diam velit suscipit diam, tincidunt elementum velit nibh id nunc. Maecenas laoreet tempus semper.</p>
  <span class="arrow down"></span>
</section>
<div class="media" role="img" aria-label="Businessman standing before a city skyline under a cloudy sky" style="left:99px;top:800px;width:417px;height:238px;background:linear-gradient(180deg,#6f7478,#9ea2a5 55%,#c9cbcc)"></div>

<div class="media" role="img" aria-label="Stethoscope resting on an open book" style="left:527px;top:602px;width:261px;height:321px;background:linear-gradient(160deg,#6a5444,#c9ab82 55%,#8a6d4e)"></div>
<section class="tile" style="left:798px;top:602px;width:303px;height:321px">
  <h2>Medical<br>Education</h2>
  <p>Aliquam efficitur, ante quis varius gravida, diam velit suscipit diam, tincidunt elementum velit nibh id nunc. Maecenas laoreet tempus semper. Aliquam a sodales magna. Donec nec velit a turpis molestie molestie quis sit amet neque.</p>
  <span class="arrow left" style="top:156px"></span>
</section>

<section class="tile" style="left:527px;top:936px;width:261px;height:321px">
  <h2>Medical<br>Societies</h2>
  <p>Aliquam efficitur, ante quis varius gravida, diam velit suscipit diam, tincidunt elementum velit nibh id nunc. Maecenas laoreet tempus semper. Aliquam a sodales magna.</p>
  <span class="arrow right" style="top:158px"></span>
</section>
<div class="media" role="img" aria-label="Group of medical professionals gathered around a tablet" style="left:798px;top:936px;width:303px;height:321px;background:linear-gradient(135deg,#d9d4cc,#b8a898 50%,#7c6f6a)"></div>

<section class="tile" style="left:99px;top:1050px;width:417px;height:519px">
  <h2>Patients Education for Pharmaceutical Companies</h2>
  <p style="margin-top:12px">Morbi ut risus in lectus vulputate viverra eget non turpis. Vestibulum a sodales magna. Quisque ut magna lobortis, interdum augue vel, luctus tortor. Sed quis nisl ut purus facilisis pellentesque a vel neque. Cras rhoncus diam tellus, sed porta ipsum ultrices vel. Donec massa odio, eleifend non tortor eu, gravida dictum nisi. Nulla et turpis a turpis mattis sodales. Mauris eget mauris magna. Donec massa elit, efficitur et leo quis, vehicula tincidunt mauris. Vestibulum ante ipsum primis in faucibus orci luctus et ultrices posuere cubilia Curae; Cras tempus male-suada lacus ultrices pulvinar.</p>
  <span class="arrow right" style="top:242px"></span>
</section>
<div class="media" role="img" aria-label="Doctor explaining a spine model to a patient" style="left:527px;top:1269px;width:574px;height:300px;background:linear-gradient(120deg,#c9c2b8,#ece8e2 50%,#b49a80)"></div>

<div class="media" role="img" aria-label="Cupped hands holding a chain of paper figures in warm light" style="left:99px;top:1581px;width:417px;height:323px;background:radial-gradient(circle at 50% 55%,#e79a7a,#8a3b2a 35%,#0c0c0c 70%)"></div>
<section class="tile" style="left:527px;top:1581px;width:574px;height:323px">
  <h2>Patient Advocacy Groups</h2>
  <p>Donec pharetra, odio non elementum ornare, mi sapien eleifend sem, luctus lacinia lectus enim quis mi. Duis non felis bibendum, luctus orci a, suscipit arcu. Nullam vitae lectus diam. Nulla ultricies sit amet nibh ut con-sectetur. Ut odio nunc, lobortis quis odio id, ornare consectetur erat. Ut tincidunt sed elit nec eleifend. In hac habitasse platea dictumst. Donec sit amet laoreet massa. Sed in ipsum sed quam ultricies interdum. Aliquam in felis blandit, malesuada felis et, mattis ex.</p>
  <span class="arrow left" style="top:143px"></span>
</section>

<div class="contacts">
  <svg class="contact-icon" style="left:142px" viewBox="0 0 24 24"><path d="M5 2h14v20H5zM8 6h8v2H8zm0 4h8v2H8zm0 4h6v2H8z" fill-rule="evenodd"/></svg>
  <div class="contact-box" style="left:185px;width:262px">55, Building name, Street name,<br>City - Zipcode</div>
  <svg class="contact-icon" style="left:496px" viewBox="0 0 24 24"><path d="M3 5c6-4 12-4 18 0l-2 3-3-1V5H8v2L5 8zM6 11h12v10H6zm2 2v2h2v-2zm3 0v2h2v-2zm3 0v2h2v-2zm-6 4v2h2v-2zm3 0v2h2v-2zm3 0v2h2v-2z"/></svg>
  <div class="contact-box" style="left:540px;width:105px">555 014 2290</div>
  <svg class="contact-icon" style="left:676px" viewBox="0 0 24 24"><path d="M7 2h10v6H7zM3 9h18v9h-3v4H6v-4H3zm5 7v4h8v-4z"/></svg>
  <div class="contact-box" style="left:718px;width:106px">555 014 2290</div>
  <svg class="contact-icon" style="left:864px" viewBox="0 0 24 24"><path d="M7 2h10v6H7zM3 9h18v9h-3v4H6v-4H3zm5 7v4h8v-4z"/></svg>
  <div class="contact-box" style="left:907px;width:148px">info@veltrimo.com</div>
</div>

<div class="divider"></div>
<nav class="footer-nav">Home<span>|</span>About us<span>|</span>Services<span>|</span>Contact us</nav>
<p class="copyright">Copyright © 2014 &nbsp;veltrimo. &nbsp;All rights reserved.</p>
<div class="social" style="left:531px"></div>
<div class="social" style="left:582px"></div>
<div class="social" style="left:630px"></div>
</body>
</html>
```